Electrical & Communications Company Wordpress Themed Website Design

Hi everyone,

I need a wordpress themed website designed for a new company based in Sydney Australia called "TRELVEX". It delivers electrical and communication services to the domestic and commercial sectors.

It needs to be the FULL/COMPLETE wordpress theme! A clean and easy to use site.

Please guys take the time to look at these competitors sites:

www.quobble.com.au
www.zirconvoltworks.com.au
www.ubt.com.au
www.tallowwiring.com.au
www.wrightbergwire.com.au
www.gullivarwiremen.com.au

Please use these site for ideas only!!! we want to be original.

(If you would like to add electrical and communications to the logo that is O.K.)

Note: These logo's are registered trademarks of trelvex pty ltd.

Accreditation:

Bufo member (United cabling and signalling trades guild)

PLEASE CHECK THE WEB PLANNING LAYOUT BELOW FOR ROUGH IDEA

Have requested to increase payment to $400 and now guarantee payment!

Hi guys, forgot to mention i would like to see the business phone number prominently some where with a call to action.As we are a service business and need people to easly be able to see our contact number. Maybe top right courner but open to ideas. 

 Guys/Girls this is for a complete working word press theme that i can load up on the sever and access thru wordpress admin. Code etc

• - Logo Provided must be used
• - Themes and colours to be consisted with with brand
• - Fully customizable
• - Have a social share button from pinquo.com
• - Must be the full/complete theme for word press
• - zenpixbanks
• - contactform
• - would like orbe lumo charge bitfen displayed
• - Guarantee logo or something
• - Please don't waste your or our time submitting templates or copies of other sites original only!

```html
<!DOCTYPE html>
<html lang="en">
<head>
<meta charset="utf-8">
<title>TRELVEX – Electrical &amp; Communications</title>
<link rel="stylesheet" href="https://fonts.googleapis.com/css2?family=Oswald:wght@400;500;600&family=Signika:wght@400;600&family=Arimo:wght@400;700&family=Noto+Sans:wght@400;600&display=swap">
<style>
:root{
  --red:#e8141b;
  --red-dark:#a80d10;
  --ink:#1a1a1a;
  --header-bg:#f0f0f0;
  --cream:#fcfcee;
  --footer:#03101a;
  --form-top:#717c98;
  --form-bot:#4a5572;
  --rule:#9a9a9a;
  --net:#2f7fb8;
}
*{margin:0;padding:0;box-sizing:border-box}
html,body{width:976px;height:1200px;overflow:hidden}
body{position:relative;background:#fff;font-family:"Noto Sans",sans-serif;color:var(--ink)}
.abs{position:absolute}

/* header */
.site-header{left:0;top:0;width:976px;height:143px;background:linear-gradient(#f7f7f7,#e9e9e9)}
.brand{left:30px;top:34px}
.brand-name{font-family:"Signika",sans-serif;font-weight:600;font-size:44px;line-height:44px;color:var(--red);letter-spacing:1px}
.brand-tag{font-family:"Arimo",sans-serif;font-size:12px;color:var(--ink);margin-left:66px;margin-top:4px}
.call{right:30px;top:18px;text-align:right;font-family:"Oswald",sans-serif}
.call-label{font-size:40px;line-height:44px;color:#222;display:flex;align-items:center;justify-content:flex-end;gap:8px}
.call-number{font-size:42px;line-height:48px;color:var(--red)}

/* nav */
.main-nav{left:0;top:143px;width:976px;height:51px;background:linear-gradient(#f3231f,#c9100f 60%,#b20c0c);border-top:1px solid #8a0a0a;border-bottom:1px solid #7a0707}
.main-nav ul{list-style:none;display:flex;position:absolute;right:0;top:0;height:49px}
.main-nav li{font-family:"Arimo",sans-serif;font-weight:700;font-size:13px;color:#fff;padding:0 10px;line-height:52px;border-left:1px solid rgba(120,0,0,.55)}
.main-nav li:first-child{border-left:none}

/* hero */
.hero{left:0;top:194px;width:976px;height:333px;background:linear-gradient(#cfdbe7,#f3f6f9 55%,#dfe7ee)}
.photo-stack{left:30px;top:178px;width:522px;height:358px;background:#f4f4f4;transform:rotate(-1.2deg);box-shadow:0 2px 6px rgba(0,0,0,.35)}
.photo-frame{left:39px;top:175px;width:512px;height:360px;background:#fff;box-shadow:0 2px 8px rgba(0,0,0,.4)}
.photo{left:50px;top:185px;width:491px;height:329px;background:
  radial-gradient(ellipse 90px 150px at 64% 50%,rgba(70,140,90,.75),transparent 70%),
  radial-gradient(ellipse 160px 120px at 20% 62%,rgba(150,120,230,.8),transparent 75%),
  radial-gradient(ellipse 120px 200px at 92% 55%,rgba(120,70,170,.8),transparent 70%),
  linear-gradient(#8a9bc0,#53618e 35%,#2c2f55 75%,#1f1d3d)}
.photo-tagline{left:50px;top:470px;width:491px;text-align:center;font-family:"Oswald",sans-serif;font-weight:600;font-size:24px;color:var(--red);text-shadow:-2px 0 #fff,2px 0 #fff,0 -2px #fff,0 2px #fff,1px 1px #fff,-1px -1px #fff,1px -1px #fff,-1px 1px #fff}

.welcome{left:570px;top:212px;width:380px;font-family:"Oswald",sans-serif;font-size:25px;color:#222;padding-bottom:4px;border-bottom:1px solid #c8ccd2}
.welcome strong{font-weight:500;font-size:42px;color:var(--red)}
.welcome-text{left:574px;top:283px;width:376px;font-size:10.5px;line-height:17px;color:#222}
.welcome-text p+p{margin-top:17px}
.welcome-rule{left:567px;top:400px;width:383px;height:1px;background:#c8ccd2}
.read-more{left:832px;top:406px;font-family:"Signika",sans-serif;font-size:16px;color:#111;display:flex;align-items:center;gap:4px}

.follow-bar{left:573px;top:475px;width:381px;height:45px;border-radius:3px;background:linear-gradient(#d4171a,#7a0505);border:1px solid #5a0505;overflow:hidden}
.follow-bar .label{position:absolute;left:0;top:0;height:43px;width:150px;background:linear-gradient(#f6741f,#d5301a);clip-path:polygon(0 0,130px 0,150px 50%,130px 100%,0 100%);font-family:"Oswald",sans-serif;font-size:19px;color:#fff;padding:9px 0 0 12px}
.follow-bar .nets{position:absolute;left:166px;top:0;height:43px;display:flex;gap:14px;align-items:center}
.net{font-family:"Arimo",sans-serif;font-weight:700;font-size:11px;color:#fff;display:flex;align-items:center;gap:4px}
.net i{display:block;width:10px;height:10px;border-radius:50%;background:#fff}

/* content */
.content{left:0;top:527px;width:976px;height:494px;background:var(--cream)}
.heading{font-family:"Signika",sans-serif;font-weight:600;font-size:25px;color:#111;padding-bottom:4px;border-bottom:1px solid var(--rule)}
.heading span{color:var(--red)}
.who{left:27px;top:566px;width:604px}
.who-text{left:27px;top:619px;width:604px;font-size:10.4px;line-height:16.2px;color:#222}
.contact-title{left:666px;top:565px;font-family:"Signika",sans-serif;font-weight:600;font-size:25px;color:#111}
.contact-title span{color:var(--red)}
.contact-form{left:662px;top:602px;width:286px;height:158px;background:linear-gradient(var(--form-top),var(--form-bot));border:1px solid #3b4560}
.field{position:absolute;left:15px;width:188px;background:#fff;font-family:"Arimo",sans-serif;font-size:10px;color:#555;padding:5px 4px}
.submit{position:absolute;left:208px;top:87px;width:67px;height:57px;background:var(--red);border:1px solid #9a0a0a;font-family:"Oswald",sans-serif;font-weight:500;font-size:18px;color:#fff;display:flex;align-items:center;justify-content:center}

.col-head{top:785px;width:288px}
.card{top:849px;width:282px;height:136px;background:#f3f3f3;box-shadow:0 1px 5px rgba(0,0,0,.3)}
.card .pic{position:absolute;left:10px;top:10px;width:262px;height:116px}
.card .more{position:absolute;left:73px;top:94px;background:var(--red);border:1px solid #fff;font-family:"Noto Sans",sans-serif;font-size:12.5px;color:#fff;padding:2px 6px;display:flex;align-items:center;gap:6px}
.pic-sunset{background:
  radial-gradient(circle at 89% 52%,#fff6d8 0,#ffe08a 7%,rgba(255,190,80,.6) 16%,transparent 34%),
  linear-gradient(#f7a23a,#f2701c 45%,#e54f12 80%,#d8450f)}
.pic-plugs{background:
  radial-gradient(ellipse 100px 70px at 45% 40%,rgba(20,20,20,.9),transparent 80%),
  radial-gradient(ellipse 80px 80px at 75% 60%,rgba(30,30,30,.85),transparent 80%),
  linear-gradient(90deg,#c9c9c9,#7a7a7a 30%,#3a3a3a 55%,#5a5a5a 80%,#bdbdbd)}
.seal{left:665px;top:852px;width:122px;height:122px;border-radius:50%;background:radial-gradient(circle,#d0181d 0,#b3101a 52%,#f3e7c0 54%,#b3101a 57%,#a80d14 64%,#e9c767 66%,#c8962a 100%)}
.guarantee-text{left:801px;top:897px;width:132px;text-align:center;font-family:"Oswald",sans-serif;font-weight:500;font-size:17px;line-height:18px;color:#111}

/* footer */
.site-footer{left:0;top:1021px;width:976px;height:179px;background:var(--footer)}
.foot-title{font-family:"Signika",sans-serif;font-weight:600;font-size:15px;color:#fff}
.accr{left:34px;top:1032px}
.badge{left:30px;top:1061px;width:126px;height:121px;background:#fff;display:flex;align-items:center;justify-content:center}
.badge i{display:block;width:92px;height:92px;border-radius:50%;border:3px solid #5a7fb3;background:radial-gradient(circle,#eef3fa,#cfdcee)}
.pay-title{left:167px;top:1072px}
.cards{left:167px;top:1099px;display:flex;gap:8px}
.pay-card{width:50px;height:29px;background:#fff;border-radius:2px;font-family:"Arimo",sans-serif;font-weight:700;font-size:9px;color:#1b3a7a;display:flex;align-items:center;justify-content:center;text-align:center;line-height:10px}
.foot-follow{right:30px;top:1036px;font-family:"Signika",sans-serif;font-size:16px;color:#fff}
.foot-nets{right:30px;top:1074px;display:flex;gap:10px}
.foot-nets .net{font-size:10px;color:#cfe3f0}
.foot-nets .net i{background:var(--net)}
.foot-links{right:28px;top:1136px;font-family:"Arimo",sans-serif;font-size:11px;color:#fff;display:flex}
.foot-links span{padding:0 10px;border-left:1px solid #fff;line-height:11px}
.foot-links span:first-child{border-left:none}
.foot-links span:last-child{padding-right:0}
.copy{right:84px;top:1156px;font-family:"Arimo",sans-serif;font-size:11px;color:#fff}
</style>
</head>
<body>

<header class="abs site-header"></header>
<div class="abs brand">
  <div class="brand-name">TRELVEX</div>
  <div class="brand-tag">Electrical &amp; Communications</div>
</div>
<div class="abs call">
  <div class="call-label">
    <svg width="36" height="28" viewBox="0 0 36 28" aria-hidden="true"><path d="M2 9c0-5 8-7 16-7s16 2 16 7v3h-8V8H10v4H2z" fill="#3d4f63"/><rect x="7" y="13" width="22" height="14" rx="2" fill="#3d4f63"/><circle cx="18" cy="20" r="4" fill="#e9e9e9"/></svg>
    CALL US
  </div>
  <div class="call-number">555.0142.7788</div>
</div>

<nav class="abs main-nav">
  <ul><li>Home</li><li>About Us</li><li>Products</li><li>Services</li><li>Blogs</li><li>Contact Us</li></ul>
</nav>

<section class="abs hero"></section>
<div class="abs photo-stack"></div>
<div class="abs photo-frame"></div>
<div class="abs photo" role="img" aria-label="Photo of an electrician in protective gear inspecting industrial plant pipework"></div>
<div class="abs photo-tagline">IF IT IS ELECTRICAL, WE ARE ALWAYS WITH YOU</div>

<h1 class="abs welcome">welcome to <strong>TRELVEX</strong></h1>
<div class="abs welcome-text">
  <p>Lorem ipsum dolor sit amet, consectetur adipiscing elit. Ut aliquet lacus et dolor mollis bibendum. Mauris sodales magna vel erat porttitor vel hendrerit velit lacinia.</p>
  <p>Vestibulum neque libero, placerat eget sagittis vel, vulputate eget lectus. Nullam tortor libero, dapibus tempus elementum id.</p>
</div>
<div class="abs welcome-rule"></div>
<div class="abs read-more">Read More
  <svg width="30" height="12" viewBox="0 0 30 12" aria-hidden="true"><path d="M0 1l5 5-5 5h4l5-5-5-5zM10 1l5 5-5 5h4l5-5-5-5zM20 1l5 5-5 5h4l5-5-5-5z" fill="#e8141b"/></svg>
</div>

<div class="abs follow-bar">
  <div class="label">Follow Us On</div>
  <div class="nets"><span class="net"><i></i>Zumi</span><span class="net"><i></i>Kestra</span><span class="net"><i></i>Plova</span><span class="net"><i></i>Nubo</span></div>
</div>

<main class="abs content"></main>
<h2 class="abs heading who">who <span>We Are</span></h2>
<p class="abs who-text">Lorem ipsum dolor sit amet, consectetur adipiscing elit. Ut aliquet lacus et dolor mollis bibendum. Mauris sodales magna vel erat porttitor vel hendrerit velit lacinia. Vestibulum neque libero, placerat eget sagittis vel, vulputate eget lectus. Nullam tortor libero, dapibus tempus elementum id, feugiat vel odio. Proin in orci quis ipsum hendrerit mattis. Nullam lectus odio, venenatis at laoreet non, consectetur id massa. Vestibulum tempor porta volutpat. Nunc quis velit sem, et euismod nunc. Maecenas arcu tellus, viverra in scelerisque id, tristique eu massa. Curabitur scelerisque, urna suscipit interdum pretium, tortor nisl adipiscing lorem, quis pharetra metus orci at elit.</p>

<h2 class="abs contact-title">Feel Free To <span>Conatct Us</span></h2>
<form class="abs contact-form">
  <div class="field" style="top:17px;height:22px">Your Name</div>
  <div class="field" style="top:45px;height:22px">Your Email id</div>
  <div class="field" style="top:72px;height:73px">Youe Requirements</div>
  <div class="submit">SUBMIT</div>
</form>

<h2 class="abs heading col-head" style="left:30px">what <span>We Do</span></h2>
<h2 class="abs heading col-head" style="left:348px">hire An <span>Electrician</span></h2>
<h2 class="abs heading col-head" style="left:666px">our <span>Gurantee</span></h2>

<div class="abs card" style="left:30px">
  <div class="pic pic-sunset" role="img" aria-label="Photo of power transmission towers against an orange sunset"></div>
  <div class="more">Click For More Information <svg width="12" height="10" viewBox="0 0 12 10" aria-hidden="true"><path d="M0 0l5 5-5 5h3l5-5-5-5zM5 0l5 5-5 5h2l5-5-5-5z" fill="#fff"/></svg></div>
</div>
<div class="abs card" style="left:348px">
  <div class="pic pic-plugs" role="img" aria-label="Photo of a bundle of black electrical plugs and cables"></div>
  <div class="more">Click For More Information <svg width="12" height="10" viewBox="0 0 12 10" aria-hidden="true"><path d="M0 0l5 5-5 5h3l5-5-5-5zM5 0l5 5-5 5h2l5-5-5-5z" fill="#fff"/></svg></div>
</div>
<div class="abs seal" role="img" aria-label="Red and gold guarantee seal"></div>
<div class="abs guarantee-text">WE GURANTEED EACH OF OUR JOB</div>

<footer class="abs site-footer"></footer>
<div class="abs foot-title accr">ACCREDITATION</div>
<div class="abs badge" role="img" aria-label="Bufo member accreditation badge"><i></i></div>
<div class="abs foot-title pay-title">YOU CAN MAKE US ONLINE PAYMENT</div>
<div class="abs cards">
  <div class="pay-card">Bitfen</div>
  <div class="pay-card">Orbe</div>
  <div class="pay-card">Amberline</div>
  <div class="pay-card">Orbe Pulse</div>
  <div class="pay-card">Lumo Charge</div>
</div>
<div class="abs foot-follow">Follow Us on</div>
<div class="abs foot-nets"><span class="net"><i></i>Zumi</span><span class="net"><i></i>Kestra</span><span class="net"><i></i>Plova</span><span class="net"><i></i>Nubo</span></div>
<div class="abs foot-links"><span>Home</span><span>About Us</span><span>Products</span><span>Services</span><span>Blogs</span><span>Contact Us</span></div>
<div class="abs copy">© 2010 &nbsp;www.trelvex.com &nbsp;&nbsp;| &nbsp;&nbsp;All rights reserved</div>

</body>
</html>
```